New Business Card Design Project VORASTI-Italy

we are VORASTI-Italy
our company in the market for 3 years we are luxury cosmetic company and its about time for a facelift :)
i will like to have elegant luxurious and unique business card
that will give the person that get it a unique, luxurious and elegant impression
I'm VERY OPEN FOR NEW IDEAS , even duo i add a few files of things that i see on line and i like them

i add my logo as well
my website is VORASTI.COM
(if you would like to see the main style that we have)

Target Market(s)

adult that have money :)

Industry/Entity Type

Business

Contact Information for Business Card

Name - Paul Vorasti
Position - CEO and CO Founder
address - 4817 E Larkdale
telephone - 555-384-1962
email - paul@vorasti.com
fax - 555-384-1962
website - VORASTI.COM

Colors
000000
959595
fbee3e
ffffff

Requirements
Must have
• big logo in GOLD color
• elegant look
• impressive
Nice to have
• not must but maybe classy pattern background
• not must but maybe emblem
• maybe clear plastic business card
Should not have
• colors
• images

```html
<!DOCTYPE html>
<html lang="en">
<head>
<meta charset="utf-8">
<title>VORASTI Italy – Business Card</title>
<link href="https://fonts.googleapis.com/css2?family=Cormorant+Garamond:wght@600&family=Quicksand:wght@400;500&display=swap" rel="stylesheet">
<style>
  :root {
    --canvas-bg: #e6e4e0;
    --card-black: #1c1c1c;
    --pattern-dark: #202020;
    --pattern-light: #4a4a4a;
    --gold: #d9ad2b;
    --grey: #959595;
    --white: #ffffff;
    --card-shadow: rgba(0, 0, 0, 0.35);
  }
  * { box-sizing: border-box; margin: 0; padding: 0; }
  html, body {
    width: 1200px;
    height: 900px;
    overflow: hidden;
    background: var(--canvas-bg);
  }
  .canvas {
    position: relative;
    width: 1200px;
    height: 900px;
  }
  .card {
    position: absolute;
    left: 319px;
    width: 562px;
    height: 322px;
    background: var(--card-black);
    box-shadow: 0 10px 22px var(--card-shadow);
    overflow: hidden;
  }

  /* Front */
  .card-front { top: 70px; }
  .front-pattern {
    position: absolute;
    inset: 0;
    background: linear-gradient(120deg, var(--pattern-dark) 0%, var(--pattern-light) 48%, var(--pattern-dark) 100%);
  }
  .front-frame {
    position: absolute;
    left: 28px; top: 28px; right: 28px; bottom: 28px;
    border: 3px solid var(--gold);
  }
  .brand-circle {
    position: absolute;
    left: 50%;
    top: 50px;
    width: 110px;
    height: 110px;
    margin-left: -55px;
    border: 3px solid var(--gold);
    border-radius: 50%;
  }
  .brand-name {
    position: absolute;
    left: 0; right: 0;
    top: 178px;
    text-align: center;
    font-family: "Cormorant Garamond", serif;
    font-weight: 600;
    font-size: 48px;
    letter-spacing: 2px;
    line-height: 1;
    color: var(--gold);
  }
  .brand-rule {
    position: absolute;
    left: 50%;
    top: 244px;
    width: 250px;
    height: 3px;
    margin-left: -125px;
    background: var(--gold);
  }
  .brand-country {
    position: absolute;
    left: 0; right: 0;
    top: 255px;
    text-align: center;
    font-family: "Cormorant Garamond", serif;
    font-weight: 600;
    font-size: 19px;
    letter-spacing: 1px;
    color: var(--gold);
  }

  /* Back */
  .card-back { top: 470px; }
  .back-ring {
    position: absolute;
    left: -100px;
    top: 90px;
    width: 290px;
    height: 290px;
    border: 18px solid var(--grey);
    border-radius: 50%;
  }
  .holder { position: absolute; left: 37px; top: 26px; text-align: right; }
  .holder-name {
    font-family: "Quicksand", sans-serif;
    font-weight: 500;
    font-size: 28px;
    letter-spacing: 0.5px;
    line-height: 1;
    color: var(--gold);
  }
  .holder-role {
    margin-top: 4px;
    font-family: "Quicksand", sans-serif;
    font-weight: 400;
    font-size: 13px;
    color: var(--white);
  }
  .contact-list {
    position: absolute;
    right: 36px;
    top: 120px;
    list-style: none;
    font-family: "Quicksand", sans-serif;
    font-size: 15px;
    color: var(--white);
  }
  .contact-item {
    display: flex;
    align-items: center;
    justify-content: flex-end;
    gap: 12px;
    margin-bottom: 20px;
  }
  .contact-lines { text-align: right; line-height: 1.3; }
  .contact-icon {
    flex: none;
    width: 20px;
    height: 20px;
    border-radius: 50%;
    background: var(--gold);
    display: flex;
    align-items: center;
    justify-content: center;
  }
  .contact-icon svg { width: 12px; height: 12px; fill: var(--card-black); stroke: var(--card-black); }
</style>
</head>
<body>
<main class="canvas">

  <section class="card card-front" aria-label="Business card front">
    <div class="front-pattern" role="img" aria-label="Fine dark grey diagonal lattice pattern background"></div>
    <div class="front-frame"></div>
    <div class="brand-circle"></div>
    <h1 class="brand-name">VORASTI</h1>
    <div class="brand-rule"></div>
    <p class="brand-country">ITALY</p>
  </section>

  <section class="card card-back" aria-label="Business card back">
    <div class="back-ring"></div>
    <div class="holder">
      <h2 class="holder-name">PAUL VORASTI</h2>
      <p class="holder-role">CEO and CO Founder</p>
    </div>
    <ul class="contact-list">
      <li class="contact-item">
        <span class="contact-lines">555-384-1962<br>fax - 555-384-1962</span>
        <span class="contact-icon"><svg viewBox="0 0 12 12" stroke-width="0"><path d="M2.5 1 L4.5 1 L5.3 3.4 L4 4.4 C4.6 5.8 6 7.3 7.6 8 L8.6 6.7 L11 7.5 L11 9.5 C11 10.3 10.3 11 9.5 11 C5 10.7 1.3 7 1 2.5 C1 1.7 1.7 1 2.5 1 Z"/></svg></span>
      </li>
      <li class="contact-item">
        <span class="contact-lines">WWW.VORASTI.COM</span>
        <span class="contact-icon"><svg viewBox="0 0 12 12" fill="none" stroke-width="1.2"><circle cx="6" cy="6" r="4.8"/><path d="M1.2 6 H10.8 M6 1.2 C3.8 4 3.8 8 6 10.8 M6 1.2 C8.2 4 8.2 8 6 10.8"/></svg></span>
      </li>
      <li class="contact-item">
        <span class="contact-lines">4817 E Larkdale</span>
        <span class="contact-icon"><svg viewBox="0 0 12 12" stroke-width="0"><path d="M6 0.8 C3.8 0.8 2.3 2.4 2.3 4.5 C2.3 7.2 6 11.2 6 11.2 C6 11.2 9.7 7.2 9.7 4.5 C9.7 2.4 8.2 0.8 6 0.8 Z M6 3.1 A1.4 1.4 0 1 1 6 5.9 A1.4 1.4 0 1 1 6 3.1 Z" fill-rule="evenodd"/></svg></span>
      </li>
      <li class="contact-item">
        <span class="contact-lines">paul@vorasti.com</span>
        <span class="contact-icon"><svg viewBox="0 0 12 12" stroke-width="0"><path d="M1 2.5 H11 V9.5 H1 Z M1.6 3 L6 6.4 L10.4 3 Z" fill-rule="evenodd"/></svg></span>
      </li>
    </ul>
  </section>

</main>
</body>
</html>
```